New logo and packaging for Chicago based skincare company

Venmira needs a new logo and packaging to help in marketing our new anti-aging skincare line.

About Us
We're quirky, skin-obsessed beauty geeks with a knack for research and a love for all things skincare. Our ambition to create REAL products with exotic ingredients inspired the name Venmira which translates to peau + jolie meaning beautiful skin in french.

Our Products
We strive to do it differently. We develop high potency, natural skincare products using top of the line, novel ingredients imported from all over the globe. Our products are made in the USA and free from gluten, parabens, sulfates, and useless fillers that can't deliver.
Price range: $25-75 (moderate)

LOGO
Open to any color/typography except red and purple. Should also be: modern, feminine, cultured, neutral, vibrant, simple, timeless, and sophisticated

LABEL
Logo placed on label, but should not be the focal point of product. EGF SERUM should grab attention of quick glancers
The ideal label design pairs neutrals with brights while achieving balance between minimalism and complexity.
Incorporates some sort of unconventionality, boldness, or uniqueness without adding distraction.

Color: Mostly white or silver background with splash of color (no purple, light pinks, or red). See attached kraft color chart for direction. Bright blues (teal, cobalt, navy, sky blue, and greens are ideal)

Target Market(s)

Target audience: Socially and health conscious women, cultured, ages 25-60, seeks high quality natural products with effective ingredients.

Industry/Entity Type

Skin Care Product

Logo Text

Venmira

Font styles to use
Other font styles liked:
• Open

Colors
f6f6f6
ffffff
fdfdfd
eeeeee
fbfbfb
0255a3
3176b5
33a6d7
86cfc6

Requirements
Must have
• Packaging includes:
• 1 oz amber glass bottles with white dropper - see attached image
• Dimensions: 1.25" width by 4.1" height
• Label should wrap around bottle similar to peptide complex image and includes ingredient list; Logo should be not focal point of label
• Green (peptide complex) label shows ideal clarity
• "NuGlint" can be written in several different ways, feel free to get creative
• Label Text:
• EGF
• NUGLINT
• SERUM
• Anti-aging Skin firming Scar removal
• 1 FL OZ (30ml)
• Ingredients:
• Hamamelis Virginiana (Witch Hazel) Water, Aqua (Water), Alcohol, Glycerin, Polysorbate 20, rh-Oligopeptide-1(EGF), Caprooyl Tetrapeptide-3, Cocos Nucifera (Coconut) Fruit Juice, Lavandula Angustifolia (Lavender) Oil, Citrus
• Paradisi (Pink Grapefruit) Peel Oil*, Citrus Aurantium Dulcis (Orange) Peel Oil*, Santalum Austrocaledonicum (Sandalwood) Wood Oil, Boswellia Carterii (Frankincense) Oil, Rosa Damascena Flower Oil, Dextran, Xanthan Gum,
• Gluconolactone, Sodium Benzoate
• Directions:
• Apply a small amount of EGF serum to clean skin once or twice daily. Allow to dry. Can be used both morning and night, and under makeup. Follow with moisturizer.
• Caution: For external use only. Use only as directed. Avoid contact with eyes. If contact occurs, rinse well with water.
• Distributed by Venmira, LLC
• Munster, Indiana 46398
• Made in USA, FDA Registered lab (please use symbols for these)
Nice to have
• Either or: White space, silver, boldness, numbers, kraft colors (see attached) shapes, geometric patterns, minimalism
• Label: Incorporate shapes and dimensions with minimal/bare background
• Open to handwritten fonts if clear and easy to read
Should not have
• No more than 3-4 colors, look too busy, cursive fonts

```html
<!DOCTYPE html>
<html lang="en">
<head>
<meta charset="utf-8">
<title>NuGlint Anti Aging Serum – Label</title>
<link href="https://fonts.googleapis.com/css2?family=Great+Vibes&family=Dancing+Script:wght@500&family=Amatic+SC:wght@700&family=Didact+Gothic&display=swap" rel="stylesheet">
<style>
  :root {
    --page: #ecebea;
    --leaf: #73a655;
    --leaf-deep: #5f9446;
    --parchment: #dcd6c9;
    --stripe: #cfc8b8;
    --ink: #4a4a42;
    --script: #435d37;
    --claim: #5d6a55;
    --volume: #dbe7d0;
    --veil: rgba(255, 255, 255, 0.2);
  }
  * { box-sizing: border-box; margin: 0; padding: 0; }
  html, body { width: 1200px; height: 921px; overflow: hidden; }
  body {
    background: radial-gradient(circle at 50% 45%, #f6f5f4 0%, var(--page) 100%);
    font-family: "Didact Gothic", sans-serif;
    color: var(--ink);
    position: relative;
  }
  .label {
    position: absolute;
    left: 50px; top: 153px;
    width: 1100px; height: 615px;
    background: var(--leaf);
    border-radius: 20px;
    overflow: hidden;
  }
  .label__body {
    position: absolute;
    left: 0; right: 0; top: 140px; height: 392px;
    background: var(--parchment);
  }
  .label__rule {
    position: absolute; left: 0; right: 0; height: 5px;
    background: var(--leaf);
  }
  .label__rule--top { top: 9px; }
  .label__rule--bottom { bottom: 9px; }
  .label__front {
    position: absolute;
    left: 357px; top: 0; width: 380px; height: 100%;
    background: var(--veil);
  }
  .brand {
    position: absolute; left: 357px; width: 380px; top: 52px;
    text-align: center;
    font-family: "Didact Gothic", sans-serif;
    font-size: 34px; letter-spacing: 2px;
    color: var(--parchment);
  }
  .product-name {
    position: absolute; left: 357px; width: 380px; top: 168px;
    text-align: center;
    font-family: "Great Vibes", cursive;
    font-size: 80px; line-height: 1;
    color: var(--script);
  }
  .product-type {
    position: absolute; left: 357px; width: 380px; top: 268px;
    text-align: center;
    font-family: "Dancing Script", cursive;
    font-size: 38px;
    color: var(--script);
  }
  .flourish {
    position: absolute; left: 417px; top: 352px;
    width: 260px; height: 72px;
    border-radius: 36px;
    background: linear-gradient(90deg, rgba(115,166,85,0.15), rgba(115,166,85,0.55), rgba(115,166,85,0.15));
  }
  .claims {
    position: absolute; left: 357px; width: 380px; top: 432px;
    text-align: center;
    font-family: "Amatic SC", sans-serif;
    font-size: 36px; line-height: 44px;
    color: var(--claim);
  }
  .volume {
    position: absolute; left: 357px; width: 380px; top: 550px;
    text-align: center;
    font-family: "Amatic SC", sans-serif;
    font-size: 36px; letter-spacing: 1px;
    color: var(--volume);
  }
  .panel {
    position: absolute; top: 176px; width: 335px;
    font-size: 15.5px; line-height: 19.6px;
  }
  .panel--ingredients { left: 13px; }
  .panel--directions { left: 756px; width: 340px; }
  .panel h2 {
    font-weight: 400; font-size: 20px; line-height: 24px;
  }
  .vine {
    position: absolute; right: 12px; top: 400px;
    width: 220px; height: 110px;
    border-radius: 60px 60px 10px 60px;
    background: linear-gradient(135deg, rgba(115,166,85,0.05), rgba(115,166,85,0.4));
  }
  .vine--left {
    left: 80px; right: auto; top: 455px;
    width: 120px; height: 70px;
    border-radius: 40px;
  }
</style>
</head>
<body>
  <div class="label">
    <div class="label__body">
      <div class="label__rule label__rule--top"></div>
      <div class="label__rule label__rule--bottom"></div>
    </div>
    <div class="vine vine--left" role="img" aria-label="Green leafy vine ornament"></div>
    <div class="vine" role="img" aria-label="Green vine with flower and leaf ornament"></div>
    <div class="label__front"></div>

    <div class="brand">Venmira</div>
    <div class="product-name">NuGlint</div>
    <div class="product-type">Anti aging serum</div>
    <div class="flourish" role="img" aria-label="Green floral vine ornament"></div>
    <div class="claims">Skin Firming • Cell Renewal<br>• Scar Removal •</div>
    <div class="volume">1 FL OZ (30ML)</div>

    <section class="panel panel--ingredients">
      <h2>Ingredients:</h2>
      <p>Hamamelis Virginiana (Witch Hazel) Water, Aqua (Water), Alcohol, Glycerin, Polysorbate 20, rh-Oligopeptide-1(EGF), Caprooyl Tetrapeptide-3, Cocos Nucifera (Coconut) Fruit Juice, Lavandula Angustifolia (Lavender) Oil, Citrus, Paradisi (Pink Grapefruit) Peel Oil*, Citrus Aurantium Dulcis (Orange) Peel Oil*, Santalum Austrocaledonicum (Sandalwood) Wood Oil, Boswellia Carterii (Frankincense) Oil, Rosa Damascena Flower Oil, Dextran, Xanthan Gum, Gluconolactone, Sodium Benzoate</p>
    </section>

    <section class="panel panel--directions">
      <h2>Directions:</h2>
      <p>Apply a small amount of EGF serum to clean skin once or twice daily. Allow to dry. Can be used both morning and night, and under makeup. Follow with moisturizer.</p>
      <h2>Caution:</h2>
      <p>For external use only. Use only as directed. Avoid contact with eyes. If contact occurs, rinse well with water.</p>
    </section>
  </div>
</body>
</html>
```